Stellenanzeige für eine Zahnarztpraxis
Zielgruppe
Erstellung einer Stellenanzeige :
Wir sind eine moderne Zahnarztpraxis, arbeiten auf höchsten Niveau und haben zufriedene und anspruchsvolle Patienten.
Wir achten auf Details, Ästhetik und pflegen einen freundlichen Umgang miteinander.
Mein Bruder Dr. Tobias Wrensch und ich, Jonas Wrensch, sind Inhaber der Praxis und beide Mitte 30. Wir haben ein junges Team und suchen neue Mitarbeiterinnen in der Verwaltung & Prophylaxe, da wir unsere Praxis vergrößern, die zuverlässig sind und qualitativ hochwertig arbeiten.
Unsere professionellen Zahnreinigung sowie das Bleaching erfolgt auf höchsten Niveau mit der aktuell besten Technik. Die Mitarbeiterinnen in der Prophylaxe arbeiten eigenständig und haben ihren eigenen Raum.
Die Stellenanzeige:
Unsere Zielgruppe sind zahnmedizinische Fachangestellte (ZFA) in der Prophylaxe sowie in der Verwaltung.
Wir suchen:
1) Prophylaxe Mitarbeiterin
2) Zahnmedizinische Prophylaxeassistentin (ZMP)
3) Dentalhygienikerin (DH)
4) Zahnmedizinische Verwaltungsassistentin (ZMV) & Betriebswirtin
Aufgabenstellung
Generell sind wir bei dem Design offen für neue Ideen. Wir liefern ein paar Fotos unserer Praxis, die eingearbeitet werden können. Alternativ sind passende STOCK Bilder möglich.
Gern kann unsere Homepage (www.zahnaerzte-am-lindenbogen) zur Inspiration herangezogen werden. Wir haben auch eine aktuelle Anzeige geschaltet, die wir ersetzen möchten. Es lohnt sich, diese anzusehen, um einen Gesamteindruck zu erhalten.
https://www.fundusmarkt-beispiel.de/s-inserat/zmp-zmv-zfa-betriebswirtin-m-w-d-fuer-unsere-digitale-zahnarztpraxis-in-der-stadtmitte-wir-sind-direkt-am-ruhigen-lindengarten-zentral-im-modernen-lindenbogen/7813064452-316-5027
Folgende Informationen finden wir für die Anzeige relevant:
- Praxislogo
- Homepage QR Code oder URL (Zahnaerzte-amLindenbogen.de) & e-Mailadresse der Praxis
- Ggf. Handynummer für den schnellen Kontakt: 0176-908172
- Ggf. Ein sympathisches Foto das Lächeln zeigt (neue Ideen sind willkommen)
- Unser Gesuch:
- Prophylaxe Mitarbeiterin
- Zahnmedizinische Prophylaxeassistentin (ZMP)
- Dentalhygienikerin (DH)
- ZMV / Betriebswirtin
Wichtig:
Da es bereits unzählige Stellenanzeigen in diesem Bereich gibt, wollen wir uns durch folgendes unterscheiden:
- Wir bieten die Übernahme der Kosten zur Weiterbildung zur ZMP oder zur DH an.
- Weitere Vorteile siehe unten (Liste)
Format:
Die Anzeige soll insbesondere bei Fundus Marktbrett & auf Bildfluss veröffentlich werden.
Nur als Inspiration zur Gestaltung - Bisher haben wir folgende Vorteile beworben:
✅ moderne, digitalisierte Praxis mit Wohlfühl-Atmosphäre
✅ überdurchschnittliche Bezahlung
✅ eigener Stellplatz an der Praxis
✅ kostenloses Ticket für Bus & Bahn
✅ vermögenswirksame Leistungen
✅ keine Überstunden
✅ zusätzlich monatliche Gutscheinkarte on Top

```html
<!DOCTYPE html>
<html lang="de">
<head>
<meta charset="utf-8">
<title>Stellenanzeige – Zahnärzte am Lindenbogen</title>
<link rel="stylesheet" href="https://fonts.googleapis.com/css2?family=Josefin+Sans:wght@300;400;600;700&display=swap">
<style>
  :root {
    --cream: #f3efd6;
    --brown: #5b3f2b;
    --paper: #f7f5ee;
    --ink: #4a3626;
    --page: #ffffff;
  }
  * { box-sizing: border-box; margin: 0; padding: 0; }
  html, body { width: 1200px; height: 577px; overflow: hidden; background: var(--page); }
  body { position: relative; font-family: "Josefin Sans", sans-serif; }
  .panel { position: absolute; top: 0; width: 577px; height: 577px; overflow: hidden; }
  .panel--jobs { left: 0; }
  .panel--benefits { left: 623px; }
  .photo { position: absolute; inset: 0; }
  .photo--team {
    background:
      radial-gradient(ellipse 130px 170px at 450px 250px, #e6cfa6 0%, rgba(230,207,166,0) 100%),
      radial-gradient(ellipse 150px 190px at 480px 470px, #4a4f5c 0%, rgba(74,79,92,0) 100%),
      linear-gradient(100deg, #d9c9a4 0%, #d3cdb2 45%, #b8bcb0 70%, #c9b98f 100%);
  }
  .photo--building {
    background:
      linear-gradient(180deg, rgba(200,195,165,0) 0%, rgba(200,195,165,0) 100%),
      radial-gradient(ellipse 220px 300px at 330px 320px, #9a6c4f 0%, rgba(154,108,79,0) 100%),
      linear-gradient(90deg, #d8cfa8 0%, #c9b38d 35%, #a9896a 65%, #a7bcc0 100%);
  }
  .veil { position: absolute; inset: 0; background: linear-gradient(90deg, rgba(232,222,190,.55), rgba(232,222,190,.15)); }
  .logo-tab {
    position: absolute; top: 0; right: 0; width: 110px; height: 86px;
    background: var(--paper); border-bottom-left-radius: 26px;
    display: flex; flex-direction: column; align-items: center; justify-content: center; gap: 2px;
    color: var(--ink); text-align: center;
  }
  .logo-tab__name { font-size: 11.5px; font-weight: 400; line-height: 1; }
  .logo-tab__sub { font-size: 7px; font-weight: 400; line-height: 1; }
  .headline { position: absolute; left: 60px; font-weight: 300; color: var(--cream); line-height: .95; letter-spacing: 1px; }
  .headline--dubist { top: 62px; font-size: 76px; }
  .roles { position: absolute; left: 59px; top: 130px; font-size: 54px; font-weight: 300; color: var(--brown); letter-spacing: 1px; }
  .roles-question { position: absolute; left: 62px; top: 186px; font-size: 15.5px; color: var(--brown); }
  .badge {
    position: absolute; left: 58px; top: 218px; width: 207px; height: 55px;
    border: 2px solid var(--cream); border-radius: 8px;
    color: var(--cream); font-weight: 700; font-size: 13.5px; letter-spacing: 2px;
    display: flex; flex-direction: column; justify-content: center; padding-left: 18px; line-height: 1.4;
  }
  .search { position: absolute; left: 62px; top: 306px; color: var(--brown); }
  .search__title { font-size: 18px; font-weight: 700; margin-bottom: 6px; }
  .search__list { list-style: disc; padding-left: 29px; font-size: 17px; line-height: 23.5px; }
  .footer {
    position: absolute; bottom: 0; left: 37px; width: 507px; height: 63px;
    background: var(--paper); border-top-left-radius: 28px; border-top-right-radius: 28px;
    color: var(--ink); font-size: 11.2px; line-height: 15.5px; text-align: center; padding-top: 9px;
  }
  .panel--benefits .footer { left: 38px; width: 506px; }
  .headline--benefits { top: 62px; font-size: 76px; left: 60px; }
  .intro { position: absolute; left: 59px; top: 210px; width: 480px; color: var(--cream); font-size: 15.3px; line-height: 22.4px; }
  .benefits { position: absolute; left: 59px; top: 346px; width: 500px; display: grid; grid-template-columns: 213px 1fr; row-gap: 19px; color: var(--cream); font-size: 12.4px; }
  .benefit { display: flex; align-items: center; gap: 16px; height: 21px; white-space: nowrap; }
  .benefit svg { flex: none; width: 11px; height: 21px; }
</style>
</head>
<body>

<section class="panel panel--jobs">
  <div class="photo photo--team" role="img" aria-label="Lächelnde Mitarbeiterinnen der Praxis im hellen Behandlungsraum"></div>
  <div class="veil"></div>
  <div class="logo-tab"><span class="logo-tab__name">Zahnärzte</span><span class="logo-tab__sub">am Lindenbogen</span></div>
  <h1 class="headline headline--dubist">DU BIST</h1>
  <p class="roles">ZMP/DH/ZMV</p>
  <p class="roles-question">oder willst eine werden?</p>
  <div class="badge"><span>KOSTENÜBERNAHME</span><span>BEI WEITERBILDUNG</span></div>
  <div class="search">
    <p class="search__title">Wir suchen (m/w/d)</p>
    <ul class="search__list">
      <li>Prophylaxe MA</li>
      <li>ZMP / DH</li>
      <li>ZMV &amp; Betriebswirtin</li>
    </ul>
  </div>
  <footer class="footer">
    Wir freuen uns auf Dich! | Sende deine Bewerbung an: info@zahnaerzte-lb.de<br>
    Zahnärzte am Lindenbogen | Dr. Tobias &amp; Jonas Wrensch | Lindenallee 14,<br>
    45127 Musterstadt | www.zahnaerzte-am-lindenbogen.de | Praxis: 0231 - 48160
  </footer>
</section>

<section class="panel panel--benefits">
  <div class="photo photo--building" role="img" aria-label="Modernes Klinkergebäude der Praxis vor blauem Himmel"></div>
  <div class="veil"></div>
  <div class="logo-tab"><span class="logo-tab__name">Zahnärzte</span><span class="logo-tab__sub">am Lindenbogen</span></div>
  <h2 class="headline headline--benefits">DEINE<br>BENEFITS</h2>
  <p class="intro">Wir legen Wert auf Qualität und bieten ein positives Arbeitsklima, Anerkennung, faire Bezahlung, Zusatzleistungen sowie Weiterbildungsmöglichkeiten. Werde Teil unseres Teams und entwickle Dich beruflich in unserer Praxis mit familiärem Ambiente weiter.</p>
  <ul class="benefits">
    <li class="benefit"><svg viewBox="0 0 11 21"><path d="M0 0 L11 10.5 L0 21 Z" fill="var(--cream)"/></svg>Freundliches Arbeitsklima</li>
    <li class="benefit"><svg viewBox="0 0 11 21"><path d="M0 0 L11 10.5 L0 21 Z" fill="var(--cream)"/></svg>Zentrale Lage am Lindengarten</li>
    <li class="benefit"><svg viewBox="0 0 11 21"><path d="M0 0 L11 10.5 L0 21 Z" fill="var(--cream)"/></svg>Keine Überstunden</li>
    <li class="benefit"><svg viewBox="0 0 11 21"><path d="M0 0 L11 10.5 L0 21 Z" fill="var(--cream)"/></svg>PKW Stellplatz | ÖPNV Ticket</li>
    <li class="benefit"><svg viewBox="0 0 11 21"><path d="M0 0 L11 10.5 L0 21 Z" fill="var(--cream)"/></svg>Überdurchschnittliches Gehalt</li>
    <li class="benefit"><svg viewBox="0 0 11 21"><path d="M0 0 L11 10.5 L0 21 Z" fill="var(--cream)"/></svg>Monatliche Gutscheinkarte</li>
    <li class="benefit"><svg viewBox="0 0 11 21"><path d="M0 0 L11 10.5 L0 21 Z" fill="var(--cream)"/></svg>Flexible Urlaubsgestaltung</li>
    <li class="benefit"><svg viewBox="0 0 11 21"><path d="M0 0 L11 10.5 L0 21 Z" fill="var(--cream)"/></svg>Vermögenswirksame Leistungen</li>
  </ul>
  <footer class="footer">
    Wir freuen uns auf Dich! | Sende deine Bewerbung an: info@zahnaerzte-lb.de<br>
    Zahnärzte am Lindenbogen | Dr. Tobias &amp; Jonas Wrensch | Lindenallee 14,<br>
    45127 Musterstadt | www.zahnaerzte-am-lindenbogen.de | Praxis: 0231 - 48160
  </footer>
</section>

</body>
</html>
```